Menu Design Project

Bel Roux hair and beauty service menu
we need a menu to display a handful of our services to give our customers an idea of our pricing

Cutting
Ladies cuts from $35
Men's cuts from $25
All cuts are included with a wash and dry off

Velora colours
All over colours start from $55
price will vary depending upon length and thickness of hair

Foiling
starts from $50
Price will vary depending upon length of hair

Toners
from $30

Blowdries
from $35

Upstyling
wedding styling from $45
Please enquire for special occasion styling also

Beauty Services

Waxing
Eyebrow wax and shape $17.50
Lip $10
Chin/sides $20
Legs from $25
Bikini $20
XX $30
XXX $45
Back from $25
Chest from $25

Eyes
Eyebrow tinting $15
Eyelash tinting $20
Eyelash extensions from $90

Derminia facials
Express facial $45
Deluxe facial $95

Acrylic nails
full set $60
Gel polish $35
Manicures from $35
Pedicures from $45

can provide logo and other images to help

Industry/Entity Type

Hair

Requirements
Must have
• must be called a service menu
must be eye catching and memorable but not excessive
Nice to have
• postcard style size hair menu on one side
beauty menu on the other side
elegant classy design
Should not have
• must not be called a price list
stay away from traditional price list style in terms of folding out leaflet

```html
<!DOCTYPE html>
<html lang="en">
<head>
<meta charset="utf-8">
<title>Bel Roux Service Menu</title>
<link href="https://fonts.googleapis.com/css2?family=Crimson+Text&family=Pinyon+Script&display=swap" rel="stylesheet">
<style>
  :root {
    --page: #ffffff;
    --panel: #1d1d1d;
    --panel-deep: #141414;
    --pattern: #2c2c2c;
    --ink: #ffffff;
    --ink-soft: #e8e8e8;
  }
  * { margin: 0; padding: 0; box-sizing: border-box; }
  html, body { width: 1200px; height: 867px; overflow: hidden; background: var(--page); }
  body { position: relative; font-family: "Crimson Text", Georgia, serif; color: var(--ink); }

  .menu-card { position: absolute; overflow: hidden; }
  .card-hair { left: 77px; top: 68px; width: 513px; height: 730px; }
  .card-beauty { left: 608px; top: 70px; width: 509px; height: 723px; }

  .damask {
    position: absolute; inset: 0;
    background: radial-gradient(ellipse at 50% 40%, var(--pattern) 0%, var(--panel) 70%);
  }
  .list-field { position: absolute; background: var(--panel-deep); opacity: .85; }

  .brand-name {
    position: absolute;
    font-family: "Pinyon Script", cursive;
    font-size: 34px; line-height: 40px;
    color: var(--ink);
  }
  .menu-title {
    position: absolute;
    font-family: "Pinyon Script", cursive;
    font-size: 21px; line-height: 24px;
    letter-spacing: 1px;
    color: var(--ink);
  }
  .section-title {
    position: absolute;
    font-family: "Pinyon Script", cursive;
    font-size: 17px; line-height: 20px;
    font-weight: 400;
    letter-spacing: .5px;
  }
  .item, .price {
    position: absolute;
    font-size: 13px; line-height: 16px;
    color: var(--ink-soft);
    white-space: nowrap;
  }
  .price-right { text-align: right; }
  .note {
    position: absolute;
    font-size: 10px; line-height: 14px;
    color: var(--ink-soft);
    white-space: nowrap;
  }
</style>
</head>
<body>

<section class="menu-card card-hair">
  <div class="damask" role="img" aria-label="Dark grey damask pattern background"></div>
  <div class="list-field" style="left:56px; top:157px; width:399px; height:510px;"></div>
  <div class="brand-name" style="left:55px; top:38px;">Bel Roux</div>
  <h1 class="menu-title" style="left:226px; top:88px;">Hair service menu</h1>
</section>

<section class="menu-card card-beauty">
  <div class="damask" role="img" aria-label="Dark grey damask pattern background"></div>
  <div class="list-field" style="left:32px; top:148px; width:450px; height:470px;"></div>
  <div class="brand-name" style="left:47px; top:38px;">Bel Roux</div>
  <h1 class="menu-title" style="left:220px; top:88px;">Beauty service menu</h1>
</section>

<!-- Hair services -->
<h2 class="section-title" style="left:151px; top:233px;">Cutting</h2>
<span class="item" style="left:152px; top:259px;">Ladies cuts</span>
<span class="price price-right" style="right:690px; top:259px;">from $35</span>
<span class="item" style="left:152px; top:275px;">Men's cuts</span>
<span class="price price-right" style="right:690px; top:275px;">from $25</span>
<p class="note" style="left:152px; top:299px;">(all cuts are included with a wash and dry off)</p>

<h2 class="section-title" style="left:151px; top:357px;">Velora colours</h2>
<span class="item" style="left:152px; top:381px;">All over colours start</span>
<span class="price price-right" style="right:690px; top:381px;">from $55</span>
<p class="note" style="left:152px; top:405px;">(price will vary depending upon length and thickness of hair)</p>

<h2 class="section-title" style="left:151px; top:458px;">Foiling</h2>
<span class="price price-right" style="right:687px; top:460px;">starts from $50</span>
<p class="note" style="left:152px; top:484px;">(price will vary depending upon length of hair)</p>

<h2 class="section-title" style="left:151px; top:537px;">Toners</h2>
<span class="price price-right" style="right:690px; top:540px;">from $30</span>

<h2 class="section-title" style="left:151px; top:595px;">Blowdries</h2>
<span class="price price-right" style="right:690px; top:597px;">from $35</span>
<p class="note" style="left:152px; top:621px;">(price will vary depending upon length and thickness of hair)</p>

<h2 class="section-title" style="left:151px; top:683px;">Upstyling</h2>
<span class="item" style="left:152px; top:708px;">wedding styling</span>
<span class="price price-right" style="right:690px; top:708px;">from $45</span>
<p class="note" style="left:152px; top:732px;">(please enquire for special occasion styling also)</p>

<!-- Waxing -->
<h2 class="section-title" style="left:656px; top:243px;">Waxing</h2>
<span class="item" style="left:657px; top:271px;">Eyebrow wax and shape</span><span class="price" style="left:833px; top:271px;">$17.50</span>
<span class="item" style="left:657px; top:294px;">Lip</span><span class="price" style="left:833px; top:294px;">$10</span>
<span class="item" style="left:657px; top:317px;">Chin/sides</span><span class="price" style="left:833px; top:317px;">$20</span>
<span class="item" style="left:657px; top:340px;">Legs</span><span class="price" style="left:805px; top:340px;">from $25</span>
<span class="item" style="left:657px; top:364px;">Bikini</span><span class="price" style="left:833px; top:364px;">$20</span>
<span class="item" style="left:657px; top:387px;">XX</span><span class="price" style="left:833px; top:387px;">$30</span>
<span class="item" style="left:657px; top:410px;">XXX</span><span class="price" style="left:833px; top:410px;">$45</span>
<span class="item" style="left:657px; top:433px;">Back from</span><span class="price" style="left:833px; top:433px;">$25</span>
<span class="item" style="left:657px; top:457px;">Chest from</span><span class="price" style="left:833px; top:457px;">$25</span>

<!-- Facials -->
<h2 class="section-title" style="left:908px; top:392px;">Derminia facials</h2>
<span class="item" style="left:908px; top:420px;">Express facial</span><span class="price" style="left:1041px; top:420px;">$45</span>
<span class="item" style="left:908px; top:443px;">Deluxe facial</span><span class="price" style="left:1041px; top:443px;">$95</span>

<!-- Eyes -->
<h2 class="section-title" style="left:660px; top:552px;">Eyes</h2>
<span class="item" style="left:660px; top:581px;">Eyebrow tinting</span><span class="price price-right" style="right:343px; top:581px;">$15</span>
<span class="item" style="left:660px; top:604px;">Eyelash tinting</span><span class="price price-right" style="right:343px; top:604px;">$20</span>
<span class="item" style="left:660px; top:627px;">Eyelash extensions</span><span class="price price-right" style="right:343px; top:627px;">from $90</span>

<!-- Nails -->
<h2 class="section-title" style="left:905px; top:552px;">Acrylic nails</h2>
<span class="item" style="left:905px; top:580px;">Full set</span><span class="price price-right" style="right:142px; top:580px;">$60</span>
<span class="item" style="left:905px; top:603px;">Gel polish</span><span class="price price-right" style="right:142px; top:603px;">$35</span>
<span class="item" style="left:905px; top:626px;">Manicures from</span><span class="price price-right" style="right:142px; top:626px;">$35</span>
<span class="item" style="left:905px; top:649px;">Pedicures from</span><span class="price price-right" style="right:142px; top:649px;">$45</span>

</body>
</html>
```